flyer/brochure design to deliver to homes (letter box delivery)

Hi I would like something designed to represent my business Hair & Make up, I have a home based salon but offer mobile services for weddings. I really like beachy colours elegant and not to busy. but open to all different designs.

I will be getting these printed up through Lumaro print the product specs are:

Document Trim Size
Horizontal
216 x 139 mm
2556 x 1642 pixels
Vertical
139 x 216 mm
1642 x 2556 pixels

Full Bleed Size
Horizontal
219 x 142 mm
2592 x 1677 pixels
Vertical
142 x 219 mm
1677 x 2592 pixels
Finished artwork should use the full bleed dimensions for best results.

I will also upload a recent business card that i have but dont have to stick to similar design

Industry/Entity Type

Salon

Requirements
Must have
• my logo (you can change the colour of my logo if you like)

would like it to have somewhere:
"look good feel great without paying silly prices"

must also have:

private home salon based in bateau bay, mobile service provided for weddings only

Im thinking I would like the price list on the back but open to what ever you submit

price list:
Ladies Cut $20
Ladies Blowdry $20 from
Mens cut $15
Full head of Foils, Toner, Cut & Blowdry $110
Half Head of Foils, Toner, Cut & Blowdry $80
Tint cut & colour $60-80
Tint with scattered foils Cut & Blowdry $70-$110

Wedding Package Hair & Make up $135pp mobile servive provided
check out our webpage for our complete pricelist

prices subject to change without notice

business details:

p: 0491 572 308
E: wbs@quorlin.com.au
W: www.willowbloomstudio.com.au

I would like it to have maybe on the front as an initial eye catcher:

Full head of foils, Toner, Cut & Blowdry $110 every day

```html
<!DOCTYPE html>
<html lang="en">
<head>
<meta charset="utf-8">
<title>Willow Bloom Studio – Flyer</title>
<link rel="stylesheet" href="https://fonts.googleapis.com/css2?family=Arimo:wght@400;700&family=Merienda:wght@400;700&display=swap">
<style>
  :root {
    --pink: #e0195f;
    --teal: #2b9a9d;
    --teal-soft: #2f7f82;
    --ink: #111111;
    --paper: #ffffff;
    --night: #1d1d1d;
    --night-deep: #141414;
    --smoke: #3a3a3a;
  }
  * { box-sizing: border-box; margin: 0; padding: 0; }
  html, body { width: 1200px; height: 779px; overflow: hidden; background: var(--paper); }
  .flyer {
    position: relative;
    width: 1200px;
    height: 779px;
    overflow: hidden;
    font-family: "Arimo", Arial, sans-serif;
    border: 1px solid var(--ink);
  }
  .masthead {
    position: absolute; left: 0; top: 0;
    width: 100%; height: 295px;
    background: var(--paper);
  }
  .brand-name {
    position: absolute; left: 44px; top: 34px;
    font-family: "Merienda", Georgia, serif;
    font-weight: 700;
    color: var(--pink);
    font-size: 62px;
    line-height: 1.12;
    letter-spacing: 1px;
  }
  .brand-dot {
    position: absolute; left: 262px; top: 228px;
    width: 22px; height: 22px; border-radius: 50%;
    background: var(--teal);
  }
  .services {
    position: absolute; left: 736px; top: 36px;
    list-style: none;
    color: var(--pink);
    font-size: 31px;
    line-height: 59px;
  }
  .services li::before { content: "•"; margin-right: 16px; }
  .web {
    position: absolute; right: 32px; top: 268px;
    font-size: 21px; color: var(--ink);
  }
  .showcase {
    position: absolute; left: 0; top: 295px;
    width: 100%; height: 484px;
    background: linear-gradient(180deg, var(--night) 0%, var(--night-deep) 100%);
  }
  .portrait-area {
    position: absolute; left: 0; top: 60px;
    width: 340px; height: 424px;
    background: radial-gradient(ellipse at 45% 45%, var(--smoke) 0%, rgba(58,58,58,0.35) 45%, rgba(29,29,29,0) 72%);
  }
  .flourish-area {
    position: absolute; left: 380px; top: 0;
    width: 820px; height: 484px;
    background: radial-gradient(ellipse at 60% 45%, rgba(80,80,80,0.45) 0%, rgba(60,60,60,0.18) 45%, rgba(29,29,29,0) 75%);
  }
  .offer {
    position: absolute; left: 68px; top: 46px;
    font-family: "Merienda", Georgia, serif;
    font-weight: 700;
    color: var(--pink);
    font-size: 53px;
    line-height: 89px;
    text-shadow: 2px 3px 3px rgba(0,0,0,0.8);
  }
  .tagline {
    position: absolute; left: 347px; top: 265px;
    font-family: "Merienda", Georgia, serif;
    color: var(--teal-soft);
    font-size: 23px;
    line-height: 38px;
  }
  .tagline span { display: block; }
  .tagline .indent { padding-left: 110px; }
  .contact {
    position: absolute; left: 88px; top: 423px;
    font-size: 25px; color: var(--paper);
    white-space: nowrap;
  }
  .contact .person {
    color: var(--teal); font-weight: 700; margin-right: 26px;
  }
</style>
</head>
<body>
<div class="flyer">
  <header class="masthead">
    <div class="brand-name">WILLOW BLOOM<br>STUDIO</div>
    <span class="brand-dot"></span>
    <ul class="services">
      <li>Hair &amp; Make Up</li>
      <li>Salon</li>
      <li>Mobile Wedding Service</li>
    </ul>
    <p class="web">www.willowbloomstudio.com.au</p>
  </header>
  <section class="showcase">
    <div class="portrait-area" role="img" aria-label="Faint silhouette of a woman with flowing hair"></div>
    <div class="flourish-area" role="img" aria-label="Large faint decorative looping flourish"></div>
    <h1 class="offer">Full head of foils, Toner, Cut &amp;<br>Blowdry $110 every day</h1>
    <p class="tagline"><span>“Look good &amp; feel great</span><span class="indent">without the price tag”</span></p>
    <p class="contact"><span class="person">MARA-JANE ELSWORTH</span>Call 0491 572 308&nbsp; or email me on wbs@quorlin.com.au</p>
  </section>
</div>
</body>
</html>
```